Billboard design - consider what a billboard is

Design a billboard using my logo - Billboard is 6m x 3m
A Billboard is advertising for my company that is on a big sign.

Has to be clean and easy to read, and ideally highlights that we are Residential and Commercial builders.

Keep it clean and easy to read

The contact number for the board is

022 583 7092
www.harbourframeworks.co.nz
info@harbourframeworks.co.nz

Doesnt have to have all contact details if it doesnt fit

Has to catch peoples attention to contact us if they need a builder

Can you please change the sign to be all white writing, with black background ?
Updates

Please consider what a billboard is...

The design needs to be suitable for a billboard..

Target Market(s)

people driving past

Industry/Entity Type

Construction

Logo Text

Wellington Builder, website email address, contact number

Colors
0054AA
0677BA
7BADD7
CADEEF
E8F1F8

Requirements
Must have
• Easy to read
Nice to have
• easy to read, can clearly see contact details

```html
<!DOCTYPE html>
<html lang="en">
<head>
<meta charset="utf-8">
<title>Harbour Frameworks Billboard</title>
<link href="https://fonts.googleapis.com/css2?family=Oswald:wght@500;600;700&display=swap" rel="stylesheet">
<style>
  :root {
    --ink: #000000;
    --paper: #ffffff;
    --stage: #eef1f4;
    --brand-blue: #4a7fc4;
    --band-light: #5b8fd6;
    --band-deep: #0d3f86;
    --sky-top: #c9dcef;
    --sky-bottom: #5d7891;
    --logo-grey: #5a5558;
  }
  * { margin: 0; padding: 0; box-sizing: border-box; }
  html, body {
    width: 1122px;
    height: 1200px;
    overflow: hidden;
    background: var(--stage);
    font-family: "Oswald", "Arial Narrow", sans-serif;
  }
  .billboard {
    position: absolute;
    left: 0;
    top: 320px;
    width: 1122px;
    height: 561px;
    overflow: hidden;
    background: var(--ink);
  }
  .billboard svg.shapes {
    position: absolute;
    inset: 0;
  }
  .logo-plate {
    position: absolute;
    left: 0;
    top: 22px;
    width: 292px;
    height: 172px;
    background: var(--paper);
    display: flex;
    align-items: center;
    padding-left: 34px;
    gap: 14px;
  }
  .logo-mark {
    width: 26px;
    height: 26px;
    background: var(--logo-grey);
    flex: none;
  }
  .logo-name {
    color: var(--brand-blue);
    font-weight: 600;
    font-size: 34px;
    line-height: 1.05;
  }
  .intro {
    position: absolute;
    left: 606px;
    top: 44px;
    font-size: 48px;
    font-weight: 600;
    color: var(--brand-blue);
    line-height: 1;
  }
  .services {
    position: absolute;
    left: 606px;
    top: 112px;
    font-size: 56px;
    font-weight: 600;
    color: var(--paper);
    line-height: 1.18;
    white-space: nowrap;
  }
  .phone {
    position: absolute;
    left: 574px;
    top: 270px;
    font-size: 84px;
    font-weight: 700;
    color: var(--paper);
    line-height: 1;
    letter-spacing: 1px;
    white-space: nowrap;
  }
  .contact-line {
    position: absolute;
    left: 606px;
    font-size: 35px;
    font-weight: 600;
    color: var(--paper);
    line-height: 1;
    white-space: nowrap;
  }
  .contact-web { top: 404px; }
  .contact-mail { top: 460px; }
</style>
</head>
<body>
  <section class="billboard">
    <svg class="shapes" width="1122" height="561" viewBox="0 0 1122 561">
      <defs>
        <linearGradient id="cityTone" x1="0" y1="0" x2="0" y2="1">
          <stop offset="0" stop-color="var(--sky-top)"/>
          <stop offset="0.6" stop-color="#8aa6c2"/>
          <stop offset="1" stop-color="var(--sky-bottom)"/>
        </linearGradient>
      </defs>
      <polygon points="0,0 560,0 545,370 270,561 0,561" fill="url(#cityTone)" role="img" aria-label="Photo of glass office towers and a tower crane seen from below against a blue sky"/>
      <polygon points="470,0 520,0 520,330 420,520" fill="var(--band-deep)"/>
      <polygon points="520,0 600,0 545,375 270,561 220,561 525,370" fill="var(--band-light)"/>
      <polygon points="600,0 1122,0 1122,561 270,561 545,375" fill="var(--ink)"/>
    </svg>

    <div class="logo-plate">
      <span class="logo-mark"></span>
      <span class="logo-name">Harbour<br>Frameworks</span>
    </div>

    <p class="intro">We are</p>
    <h1 class="services">Residential and<br>Commercial builders</h1>
    <p class="phone">022 583 7092</p>
    <p class="contact-line contact-web">www.harbourframeworks.co.nz</p>
    <p class="contact-line contact-mail">info@harbourframeworks.co.nz</p>
  </section>
</body>
</html>
```